SilverLedgerOak - Double Sided Business Card

We are looking for design options or our business cards. We are a Business Solutions and HR solutions Provider - the theme is business, for this card.

Our brand colours are represented within our logo.

Details needed to be put on the front of the business card are:

Employees name: [Sample Name]
Role: [Sample Role]

Address: Suite 4 - Level 3/48 Halloran Avenue Wrenfield NSW 2764
M: 0000 000 000
P: 1300 847 213
F: 1300 847 286
E: sample@silverledgeroak.com.au
www.silverledgeroak.com.au
Updates

Reason: Hello, could we please increase our deadline by 5 days. Thanking you, Tess

Target Market(s)

Business Owners, also Candidates looking for Employment

Industry/Entity Type

Business

Contact Information for Business Card

Role: [Sample Role]

M: 0000 000 000
P: 1300 847 213
F: 1300 847 286

Font styles to use
Sans Serif

Colors
3276b5
3176b5
0455a3
85abd2
cfdeed
ffffff
000000
1b1b1b
757575

Requirements
Must have
• Details needed to be put on the front of the business card are:
• Employees name: [Sample Name]
• Role: [Sample Role]
• Address: Suite 4 - Level 3/48 Halloran Avenue Wrenfield NSW 2764
• M: 0000 000 000
• P: 1300 847 213
• F: 1300 847 286
• E: sample@silverledgeroak.com.au
• www.silverledgeroak.com.au
Nice to have
• Simplicity, clean and professional.

```html
<!DOCTYPE html>
<html lang="en">
<head>
<meta charset="utf-8">
<title>SilverLedgerOak Business Card</title>
<link href="https://fonts.googleapis.com/css2?family=Open+Sans:wght@400;600;700;800&display=swap" rel="stylesheet">
<style>
  :root {
    --stage: #b5b5b5;
    --navy: #1b2a4a;
    --brand-blue: #0455a3;
    --rule-blue: #3276b5;
    --ink: #1b1b1b;
    --white: #ffffff;
    --back-top: #0d57a6;
    --back-bottom: #10284a;
  }
  * { box-sizing: border-box; margin: 0; padding: 0; }
  html, body { width: 1200px; height: 900px; overflow: hidden; }
  body {
    background: var(--stage);
    font-family: "Open Sans", Arial, sans-serif;
    position: relative;
  }
  .card {
    position: absolute;
    top: 306px;
    width: 440px;
    height: 272px;
    border-radius: 11px;
    box-shadow: 3px 4px 5px rgba(0,0,0,0.55);
  }
  .card-front { left: 149px; background: var(--white); }
  .card-back {
    left: 608px;
    width: 442px;
    background: linear-gradient(to bottom, var(--back-top) 0%, #0e4687 45%, var(--back-bottom) 100%);
  }

  /* front: brand block */
  .front-brand {
    position: absolute;
    left: 18px;
    top: 70px;
    width: 180px;
    text-align: center;
  }
  .brand-square {
    display: block;
    width: 44px;
    height: 44px;
    margin: 0 auto 14px;
    background: var(--brand-blue);
  }
  .front-brand .brand-name {
    font-weight: 700;
    font-size: 19px;
    color: var(--navy);
    letter-spacing: 0.2px;
  }

  .divider {
    position: absolute;
    left: 201px;
    top: 61px;
    width: 2px;
    height: 150px;
    background: var(--rule-blue);
  }

  /* front: details */
  .details {
    position: absolute;
    left: 220px;
    top: 59px;
    color: var(--ink);
  }
  .person-name {
    font-size: 14.5px;
    font-weight: 700;
    color: var(--navy);
    line-height: 18px;
    letter-spacing: 0.2px;
  }
  .person-name .surname { color: var(--brand-blue); }
  .person-role { font-size: 11.5px; line-height: 14px; margin-bottom: 7px; }
  .contact-list { list-style: none; }
  .contact-list li {
    display: flex;
    align-items: center;
    font-size: 11.5px;
    line-height: 16px;
    height: 16px;
  }
  .contact-list svg { width: 9px; height: 9px; margin-right: 6px; fill: var(--navy); flex: none; }
  .address { font-size: 11.5px; line-height: 16px; margin-top: 5px; }

  /* back */
  .back-brand {
    position: absolute;
    left: 0; right: 0;
    top: 76px;
    text-align: center;
    color: var(--white);
  }
  .back-brand .brand-square-outline {
    display: block;
    width: 50px;
    height: 50px;
    margin: 0 auto 22px;
    border: 4px solid var(--white);
  }
  .back-brand .brand-name {
    display: block;
    font-weight: 800;
    font-size: 23px;
    letter-spacing: 0.5px;
    line-height: 26px;
  }
  .tagline {
    display: block;
    margin-top: 10px;
    font-size: 7.5px;
    font-weight: 700;
    line-height: 10px;
  }
</style>
</head>
<body>

<section class="card card-front" aria-label="Business card front">
  <div class="front-brand">
    <span class="brand-square"></span>
    <span class="brand-name">SilverLedgerOak</span>
  </div>

  <div class="divider"></div>

  <div class="details">
    <p class="person-name">MARCUS <span class="surname">HALE</span></p>
    <p class="person-role">Managing Director</p>
    <ul class="contact-list">
      <li>
        <svg viewBox="0 0 10 10" aria-hidden="true"><path d="M0 3.5C1 1.5 3 1 5 1s4 .5 5 2.5L8.5 5 7 3.8H3L1.5 5zM2 6h6l1 3H1z"/></svg>
        0000 000 000
      </li>
      <li>
        <svg viewBox="0 0 10 10" aria-hidden="true"><path d="M2.5 0h5v10h-5zM3.5 1v7h3V1z"/></svg>
        1300 847 213
      </li>
      <li>
        <svg viewBox="0 0 10 10" aria-hidden="true"><path d="M1 3h8v7H1zM3 0h4v3H3zM2.5 5v1h1V5zm2 0v1h1V5zm2 0v1h1V5zm-4 2v1h1V7zm2 0v1h1V7zm2 0v1h1V7z"/></svg>
        1300 847 286
      </li>
      <li>
        <svg viewBox="0 0 10 10" aria-hidden="true"><path d="M0 2h10v6H0zM1 3l4 3 4-3z" fill-rule="evenodd"/></svg>
        sample@silverledgeroak.com.au
      </li>
      <li>
        <svg viewBox="0 0 10 10" aria-hidden="true"><circle cx="5" cy="5" r="5"/><path d="M2 4h6v1H2zm1 2h4v1H3z" fill="#fff"/></svg>
        www.silverledgeroak.com.au
      </li>
    </ul>
    <p class="address">Suite 4 - Level 3/48 Halloran<br>Avenue Wrenfield NSW 2764</p>
  </div>
</section>

<section class="card card-back" aria-label="Business card back">
  <div class="back-brand">
    <span class="brand-square-outline"></span>
    <span class="brand-name">SilverLedgerOak</span>
    <span class="tagline">Supporting growing firms to reach their fullest capacity</span>
  </div>
</section>

</body>
</html>
```